Emerging automotive detailing business

I am starting a small automotive detailing business in hopes of becoming a well-known detailer to work on high end cars. I would like a card to reflect the high quality and time I put into my work. The name of the company is Brightmere Detailing. I feel like it represents racecars getting off the line at the drag strip as well as an innuendo of "Off the Charts". I do minor paint correction such as clay barring, multi-step buffing and polishing, waxing, hand washes, etc. I am always striving to learn more and improve my work. My goal is to have total customer satisfaction. This is a female run business but I do not want it to be very girly. Elegant is okay! I have pictures of my personal kestrel attached, they do not need to be incorporated but if you can think of a cool way to use 1 or all of them, go for it!

Target Market(s)

Anyone that owns a vehicle. Preferably high end vehicles such as Valdren, Castavelli and Moretto but I will also happily work on any car, truck or suv no matter what brand.

Industry/Entity Type

Automotive

Contact Information for Business Card

Brightmere Detailing
Nora Pellworth
4715 Quillbrook Rd
Red Lion PA 17392
Cell phone- call/text- 717-555-0148
email- brightmeredetails@example.com
Instagram: @brightmeredetailing
Facebook: facebook.example/brightmeredetailing

Requirements
Must have
• Business name, my name, address, phone number. Listing that I do minor paint correction such as clay barring, multi-step buffing and polishing, waxing, hand washes, interior cleaning, and more. (This last part was in nice to haves but I have realized that I do really want it, so I moved it to must haves.) I want something that is different and eye-catching to my customers. Some people have done this very well with cards already submitted to me, but a lot have not. I didn't mess with the "look and feel bars" much because because I am pretty open to the overall design as long as it is not your basic run of the mill design.
Nice to have
• Something car related. Maybe an appointment time/date line. I do not have a logo, but if you would like to design one and incorporate it, that would be amazing!
Should not have
• Purple and Pink colors. Boring, basic, normal card.

```html
<!DOCTYPE html>
<html lang="en">
<head>
<meta charset="utf-8">
<title>Brightmere Detailing – Business Card</title>
<link rel="stylesheet" href="https://fonts.googleapis.com/css2?family=Source+Sans+3:wght@400;600;700&display=swap">
<style>
  :root {
    --stage: #ecebe9;
    --card: #ffffff;
    --brand-blue: #1565b8;
    --band-top: #1f78c4;
    --band-bottom: #0c4f9f;
    --ink-white: #ffffff;
    --label-blue: #1a5ea8;
    --service-grey: #666a70;
  }
  * { box-sizing: border-box; margin: 0; padding: 0; }
  html, body {
    width: 1200px; height: 900px; overflow: hidden;
    background: var(--stage);
    font-family: "Source Sans 3", "Helvetica Neue", Arial, sans-serif;
  }
  .canvas { position: relative; width: 1200px; height: 900px; }

  .card {
    position: absolute;
    background: var(--card);
    box-shadow: 0 6px 18px rgba(0,0,0,0.18);
    overflow: hidden;
  }
  .card--front { left: 238px; top: 62px; width: 555px; height: 342px; }
  .card--back  { left: 457px; top: 519px; width: 560px; height: 342px; }

  .wordmark {
    position: absolute;
    left: 0; right: 0;
    text-align: center;
    color: var(--brand-blue);
    font-weight: 600;
    font-size: 36px;
    line-height: 1;
    letter-spacing: 0.5px;
  }
  .card--front .wordmark { top: 62px; }
  .card--back .wordmark { top: 84px; }

  .services {
    position: absolute;
    left: 0; right: 0; top: 110px;
    text-align: center;
    color: var(--service-grey);
    font-size: 12px;
    font-weight: 400;
    letter-spacing: 1.2px;
    line-height: 17px;
    text-transform: uppercase;
  }

  .band { position: absolute; left: 0; top: 0; width: 555px; height: 342px; }

  .owner {
    position: absolute;
    right: 317px; top: 230px;
    text-align: right;
    color: var(--ink-white);
  }
  .owner__name { font-size: 19px; font-weight: 600; line-height: 1.2; margin-bottom: 6px; }
  .owner__address { font-size: 14.5px; line-height: 1.6; }

  .contact {
    position: absolute;
    left: 264px; top: 234px;
    list-style: none;
    color: var(--ink-white);
    font-size: 14.5px;
    line-height: 23px;
  }
  .contact li { display: flex; align-items: center; gap: 9px; }
  .contact svg { width: 13px; height: 13px; flex: none; }

  .appointment {
    position: absolute;
    left: 0; right: 0; top: 184px;
    color: var(--label-blue);
  }
  .appointment__title {
    text-align: center;
    font-size: 22px;
    font-weight: 700;
    margin-bottom: 16px;
  }
  .appointment__row {
    display: flex; align-items: baseline;
    font-size: 14px; font-weight: 600;
    margin-left: 92px; height: 38px;
  }
  .appointment__label { width: 60px; }
  .dots { border-bottom: 2px dotted var(--label-blue); height: 10px; }
  .dots--date { width: 313px; }
  .dots--time { width: 122px; }
  .appointment__unit { margin: 0 8px 0 10px; }
</style>
</head>
<body>
<main class="canvas">

  <section class="card card--front" aria-label="Business card front">
    <div class="wordmark">Brightmere Detailing</div>
    <p class="services">Paint Correction · Clay Barring · Multi-Step Buffing &amp; Polishing<br>Waxing · Hand Washes · Interior Cleaning · and More</p>

    <svg class="band" viewBox="0 0 555 342" aria-hidden="true">
      <defs>
        <linearGradient id="bandFill" x1="0" y1="0" x2="0" y2="1">
          <stop offset="0" stop-color="var(--band-top)"/>
          <stop offset="1" stop-color="var(--band-bottom)"/>
        </linearGradient>
      </defs>
      <path d="M0 200 Q277 132 555 200 L555 342 L0 342 Z" fill="url(#bandFill)"/>
      <path d="M0 205 Q277 140 555 205" fill="none" stroke="#ffffff" stroke-width="2.5"/>
    </svg>

    <div class="owner">
      <p class="owner__name">Nora Pellworth</p>
      <p class="owner__address">4715 Quillbrook Rd<br>Red Lion PA 17392</p>
    </div>

    <ul class="contact">
      <li>
        <svg viewBox="0 0 16 16" aria-hidden="true"><path fill="#fff" d="M3.6 1.2l2.2 2.6-1.3 1.6c.9 2 2.3 3.4 4.3 4.3l1.6-1.3 2.6 2.2-1.2 2.2C7 12.6 3.4 9 1.4 2.4z"/></svg>
        call/text- 717-555-0148
      </li>
      <li>
        <svg viewBox="0 0 16 16" aria-hidden="true"><rect x="1" y="3" width="14" height="10" fill="#fff"/><path d="M1 3l7 6 7-6" fill="none" stroke="#1565b8" stroke-width="1.4"/></svg>
        brightmeredetails@example.com
      </li>
      <li>
        <svg viewBox="0 0 16 16" aria-hidden="true"><circle cx="8" cy="8" r="6" fill="none" stroke="#fff" stroke-width="2"/></svg>
        @brightmeredetailing
      </li>
    </ul>
  </section>

  <section class="card card--back" aria-label="Business card back">
    <div class="wordmark">Brightmere Detailing</div>

    <div class="appointment">
      <p class="appointment__title">Your Next Appointment is</p>
      <div class="appointment__row">
        <span class="appointment__label">Date :</span>
        <span class="dots dots--date"></span>
      </div>
      <div class="appointment__row">
        <span class="appointment__label">Time:</span>
        <span class="dots dots--time"></span>
        <span class="appointment__unit">AM</span>
        <span class="dots dots--time"></span>
        <span class="appointment__unit">PM</span>
      </div>
    </div>
  </section>

</main>
</body>
</html>
```